Halvorsen Partners Business Card

Halvorsen Partners Civil Construction
Marcus Halvorsen
CEO
727-518-6094
Marcus@HalvorsenSiteworks.example
www.HalvorsenSiteworks.example
Site Development
Utility Construction
Excavation
40876 County Lane 19
Cedar Hollow, FL 34790

Target Market(s)

Construction and government

Industry/Entity Type

Business

Contact Information for Business Card

I want an unique design that make a statement

Number of Pages Required

1 page

Font styles to use

Colors

Designer to choose colors to be used in the design.

Requirements
Must have
• unique design, feel free to modify or change the color of my logo.
Nice to have
• extra design features like spot UV, foil accents, color edges, unique paper, or any thing that would make my card pop.
• I like the feel of the image that I attached

```html
<!DOCTYPE html>
<html lang="en">
<head>
<meta charset="utf-8">
<title>Halvorsen Partners Business Card</title>
<link href="https://fonts.googleapis.com/css2?family=Source+Sans+3:ital,wght@0,400;0,600;0,700;1,600;1,700&display=swap" rel="stylesheet">
<style>
  :root {
    --backdrop: #e9e7e4;
    --card: #f6f6f6;
    --navy: #213f86;
    --grey: #6d6e70;
    --grey-dark: #58595b;
    --ink: #4a4a4a;
  }
  * { box-sizing: border-box; margin: 0; padding: 0; }
  html, body { width: 1200px; height: 799px; overflow: hidden; }
  body {
    background: var(--backdrop);
    font-family: "Source Sans 3", "Myriad Pro", Arial, sans-serif;
    position: relative;
  }
  .card {
    position: absolute;
    top: 245px;
    width: 520px;
    height: 310px;
    background: var(--card);
    border-radius: 30px;
    overflow: hidden;
    box-shadow: 0 10px 28px rgba(0,0,0,.18);
  }
  .card--back { left: 50px; }
  .card--front { left: 630px; }

  /* back */
  .back-content {
    position: absolute; inset: 0;
    display: flex; flex-direction: column; align-items: center; justify-content: center;
    text-align: center;
  }
  .brand {
    display: flex; align-items: center; gap: 10px;
    color: var(--navy); font-weight: 700; text-transform: uppercase;
    letter-spacing: .5px; line-height: 1.05;
  }
  .brand__square { width: 14px; height: 14px; background: var(--grey); flex: none; }
  .brand--back { font-size: 26px; margin-bottom: 26px; }
  .services { color: var(--navy); font-weight: 700; font-size: 16px; line-height: 1.2; }
  .back-web { margin-top: 12px; color: var(--grey); font-size: 13px; letter-spacing: 2.5px; }

  /* front */
  .person { position: absolute; left: 34px; top: 26px; color: var(--navy); }
  .person__name { font-size: 20px; font-weight: 700; font-style: italic; }
  .person__title { font-size: 12px; font-style: italic; color: var(--ink); font-weight: 600; }
  .brand--front { position: absolute; left: 150px; top: 112px; font-size: 22px; text-align: left; }
  .contact {
    position: absolute; left: 150px; top: 178px;
    color: var(--grey-dark); font-size: 13px; line-height: 1.35;
  }
  .contact__row { display: flex; align-items: center; gap: 5px; }
  .icon { width: 11px; height: 11px; flex: none; }
  .card-band { position: absolute; left: 0; bottom: 0; width: 520px; height: 62px; }
</style>
</head>
<body>

<section class="card card--back" aria-label="Card back">
  <div class="back-content">
    <div class="brand brand--back"><span class="brand__square"></span>Halvorsen Partners</div>
    <p class="services">Site Development<br>Utility Construction Excavation</p>
    <p class="back-web">- www.HalvorsenSiteworks.example</p>
  </div>
</section>

<section class="card card--front" aria-label="Card front">
  <div class="person">
    <p class="person__name">Marcus Halvorsen</p>
    <p class="person__title">CEO</p>
  </div>

  <div class="brand brand--front"><span class="brand__square"></span><span>Halvorsen Partners<br>Civil Construction</span></div>

  <div class="contact">
    <p>40876 County Lane 19, Cedar Hollow, FL 34790</p>
    <p class="contact__row">
      <svg class="icon" viewBox="0 0 12 12"><circle cx="6" cy="6" r="6" fill="var(--navy)"/><path d="M4 3.2l1.2 1.3-.6.8c.4.8 1 1.4 1.8 1.8l.8-.6 1.3 1.2-.8 1c-2.4-.5-4.2-2.3-4.7-4.7z" fill="#fff"/></svg>
      727-518-6094
      <svg class="icon" viewBox="0 0 12 12"><circle cx="6" cy="6" r="6" fill="var(--navy)"/><rect x="3" y="4" width="6" height="4.2" fill="none" stroke="#fff" stroke-width=".9"/><path d="M3 4l3 2.4L9 4" fill="none" stroke="#fff" stroke-width=".9"/></svg>
      Marcus@HalvorsenSiteworks.example
    </p>
    <p class="contact__row">
      <svg class="icon" viewBox="0 0 12 12"><circle cx="6" cy="6" r="6" fill="var(--navy)"/><circle cx="6" cy="6" r="3.3" fill="none" stroke="#fff" stroke-width=".8"/><path d="M2.7 6h6.6M6 2.7v6.6" stroke="#fff" stroke-width=".7"/></svg>
      www.HalvorsenSiteworks.example
    </p>
  </div>

  <svg class="card-band" viewBox="0 0 520 62" preserveAspectRatio="none" aria-hidden="true">
    <polygon points="0,6 52,6 74,24 520,24 520,31 0,31" fill="var(--navy)"/>
    <polygon points="78,29 520,29 520,31 80,31" fill="#fff"/>
    <polygon points="70,33 520,33 520,62 100,62" fill="var(--grey)"/>
    <polygon points="0,31 66,31 96,62 0,62" fill="var(--navy)"/>
  </svg>
</section>

</body>
</html>
```